Book title: Wildflower: The gift of stillness!

This book is called: Wildflower: The gift of stillness!

A guide to understanding the most popular types of coaching and how to find the perfect coach for you.
The coaching industry has exploded over the past few years as the demand for them has increased. With so many different types of coaches it can be intimidating and overwhelming to find the perfect one for you. To further complicate matters, you may experience times in your life when you require multiple coaches. {Book Title} aims to quite the noise and assist you in finding the perfect coach for you. In this book, you will learn more about the different types of coaching as well as meet a hand-picked selection of coaches from the most popular coaching niches. Each featured coach has provided an exercise designed to move you powerfully forward. We encourage you to work through each exercise so you may experience firsthand the power of working with these incredible coaches.

We would like a professional and simple design. See examples included. We would like to see blood orange included in the design, please see color pallets included as well.

Target Market(s)

Corporate professionals wanting to explore the various types of coaching industry

Industry/Entity Type

Coaching - Health, business, spiritual

Font styles to use
Serif

Colors
EE7325
F08F49
F5BC92
FAE3D3
FDF4ED

Requirements
Must have
• Please include book title: Wildflower, Subtitle: The gift of stillness! Name of publishing company: Silver Lantern Publishing, Spaces for 8 author names on the front of the cover- Author Name
Nice to have
• A feminine yet corporate feel.
Should not have
• We don't want it

```html
<!DOCTYPE html>
<html lang="en">
<head>
<meta charset="UTF-8">
<title>Wildflower: The gift of stillness!</title>
<link rel="stylesheet" href="https://fonts.googleapis.com/css2?family=Oswald:wght@400;500&family=PT+Sans:wght@400;700&display=swap">
<style>
  :root {
    --stage: #333333;
    --board-dark: #262827;
    --board-mid: #343735;
    --board-light: #3d403e;
    --copper: #d8906a;
    --copper-band: #d99a78;
    --chalk-white: #f7f5f2;
    --metal-light: #cfcac6;
    --metal-dark: #6e6663;
  }
  * { margin: 0; padding: 0; box-sizing: border-box; }
  html, body {
    width: 1200px;
    height: 1200px;
    overflow: hidden;
    background: var(--stage);
  }
  .canvas {
    position: relative;
    width: 1200px;
    height: 1200px;
    display: flex;
    align-items: center;
    justify-content: center;
  }
  .cover {
    position: relative;
    width: 620px;
    height: 1080px;
    overflow: hidden;
    font-family: "PT Sans", sans-serif;
  }
  .cover-backdrop {
    position: absolute;
    inset: 0;
    background:
      radial-gradient(ellipse at 55% 45%, var(--board-light) 0%, var(--board-mid) 45%, var(--board-dark) 100%);
  }
  .whistle-image {
    position: absolute;
    left: 255px;
    top: 0;
    width: 110px;
    height: 620px;
    background: linear-gradient(180deg, var(--metal-dark) 0%, var(--metal-light) 55%, var(--metal-dark) 100%);
    border-radius: 0 0 36px 36px;
    opacity: 0.85;
  }
  .book-title {
    position: absolute;
    top: 70px;
    left: 0;
    width: 100%;
    text-align: center;
    font-family: "Oswald", sans-serif;
    font-weight: 400;
    font-size: 108px;
    line-height: 1;
    letter-spacing: 1px;
    color: var(--copper);
    text-transform: uppercase;
  }
  .title-stroke {
    position: absolute;
    top: 200px;
    left: 60px;
    width: 500px;
    height: 36px;
  }
  .subtitle {
    position: absolute;
    top: 690px;
    left: 0;
    width: 100%;
    text-align: center;
    font-weight: 400;
    font-size: 40px;
    line-height: 1.25;
    color: var(--chalk-white);
    text-transform: uppercase;
    letter-spacing: 1px;
  }
  .subtitle-stroke {
    position: absolute;
    top: 800px;
    left: 230px;
    width: 160px;
    height: 20px;
  }
  .author-list {
    position: absolute;
    list-style: none;
    font-size: 29px;
    line-height: 38px;
    color: var(--copper);
    text-transform: uppercase;
  }
  .author-list--left { top: 870px; left: 32px; }
  .author-list--right { top: 852px; left: 345px; }
  .publisher-band {
    position: absolute;
    left: 0;
    bottom: 0;
    width: 100%;
    height: 62px;
    background: var(--copper-band);
    display: flex;
    align-items: center;
    justify-content: center;
  }
  .publisher-name {
    font-size: 24px;
    letter-spacing: 3px;
    color: var(--chalk-white);
    text-transform: uppercase;
  }
</style>
</head>
<body>
<main class="canvas">
  <article class="cover">
    <div class="cover-backdrop" role="img" aria-label="Dark chalkboard texture with faint chalk smudges"></div>
    <div class="whistle-image" role="img" aria-label="Silver coach's whistle hanging from a metal chain"></div>

    <h1 class="book-title">Wildflower</h1>
    <svg class="title-stroke" viewBox="0 0 500 36" aria-hidden="true">
      <path d="M8 26 C 140 12, 330 8, 492 14" stroke="var(--copper)" stroke-width="9" fill="none" stroke-linecap="round"/>
    </svg>

    <p class="subtitle">The gift of<br>stillness!</p>
    <svg class="subtitle-stroke" viewBox="0 0 160 20" aria-hidden="true">
      <path d="M4 14 C 50 8, 110 6, 156 8" stroke="var(--copper)" stroke-width="5" fill="none" stroke-linecap="round"/>
    </svg>

    <ul class="author-list author-list--left">
      <li>Author Name</li>
      <li>Author Name</li>
      <li>Author Name</li>
      <li>Author Name</li>
    </ul>
    <ul class="author-list author-list--right">
      <li>Author Name</li>
      <li>Author Name</li>
      <li>Author Name</li>
      <li>Author Name</li>
    </ul>

    <footer class="publisher-band">
      <span class="publisher-name">Silver Lantern Publishing</span>
    </footer>
  </article>
</main>
</body>
</html>
```